Design a post card to great with NEW YEAR 2021 on behalf of a company.

Design a postcard to great with NEW YEAR 2021 on behalf of a company.

attaching the postcard with 4th Of Jully greetings and the main company logo.

We need to accomplish something that can be sent to potential and existing clients to say Happy New 2021 Year.

```html
<!DOCTYPE html>
<html lang="en">
<head>
<meta charset="utf-8">
<title>Mesa Freight Co. — Seasonal Postcards 2021</title>
<link href="https://fonts.googleapis.com/css2?family=Oswald:wght@400;600;700&family=Cinzel:wght@700&family=Anton&display=swap" rel="stylesheet">
<style>
  :root {
    --page: #eceef0;
    --front-green: #1d8a3b;
    --front-deep: #136a2b;
    --front-floor: #0f5a24;
    --scene-light: #cfe6f3;
    --gold: #c9a24a;
    --gold-light: #f0d58c;
    --back-green: #62ad68;
    --ink: #141414;
    --flag-red: #d8262f;
    --star: #f2c230;
    --white: #ffffff;
    --faint-text: rgba(20, 70, 30, 0.26);
  }
  * { margin: 0; padding: 0; box-sizing: border-box; }
  html, body {
    width: 1200px; height: 800px; overflow: hidden;
    background: var(--page);
  }
  .canvas {
    position: relative; width: 1200px; height: 800px;
    display: flex; align-items: center; justify-content: center; gap: 40px;
  }
  .postcard {
    position: relative; width: 560px; height: 410px; overflow: hidden;
    box-shadow: 0 6px 18px rgba(0,0,0,0.18);
  }

  /* Front: New Year greeting */
  .postcard--front { background: var(--front-floor); }
  .festive-scene {
    position: absolute; inset: 0 0 80px 0;
    background:
      radial-gradient(ellipse 120px 150px at 50% 40%, var(--scene-light) 0%, rgba(207,230,243,0.55) 55%, transparent 100%),
      linear-gradient(180deg, var(--front-green) 0%, var(--front-deep) 100%);
  }
  .greeting {
    position: absolute; left: 0; right: 0; top: 104px; text-align: center;
  }
  .greeting__year {
    font-family: "Cinzel", serif; font-weight: 700; font-size: 70px; line-height: 1;
    background: linear-gradient(180deg, var(--gold-light), var(--gold));
    -webkit-background-clip: text; background-clip: text; color: transparent;
  }
  .greeting__line {
    font-family: "Oswald", sans-serif; font-size: 9px; letter-spacing: 4px;
    color: var(--white); margin-top: 6px;
  }
  .greeting__company {
    font-family: "Oswald", sans-serif; font-weight: 700; font-size: 15px;
    color: var(--ink); margin-top: 40px; letter-spacing: 1px;
  }
  .front-footer {
    position: absolute; left: 0; right: 0; bottom: 0; height: 80px;
    display: flex; align-items: center; justify-content: center; padding: 0 70px;
  }
  .front-footer__text {
    font-family: "Oswald", sans-serif; font-weight: 400; font-size: 10.5px; line-height: 1.45;
    color: var(--white); text-align: center;
  }

  /* Back: Independence Day greeting */
  .postcard--back { background: var(--back-green); }
  .stamp-box {
    position: absolute; top: 18px; right: 36px; width: 62px; height: 70px;
    border: 3px solid var(--ink);
  }
  .address-lines {
    position: absolute; top: 104px; right: 30px; width: 140px;
  }
  .address-lines span {
    display: block; height: 2px; background: var(--ink); margin-bottom: 11px;
  }
  .address-lines span:first-child { margin-left: 40px; }
  .flags-artwork {
    position: absolute; top: 30px; left: 50%; transform: translateX(-50%);
    width: 96px; height: 58px;
    background: linear-gradient(90deg, var(--flag-red), #f3f3f3 50%, #2b3f8f);
    opacity: 0.85; border-radius: 4px;
  }
  .faint-year {
    position: absolute; top: 152px; left: 0; right: 0; text-align: center;
    font-family: "Anton", sans-serif; font-size: 120px; line-height: 1;
    color: var(--faint-text); letter-spacing: 6px;
  }
  .holiday {
    position: absolute; top: 154px; left: 0; right: 0; text-align: center;
  }
  .holiday__country {
    font-family: "Oswald", sans-serif; font-size: 11px; color: var(--ink); letter-spacing: 2px;
  }
  .holiday__stars { color: var(--star); font-size: 14px; letter-spacing: 3px; line-height: 1; }
  .holiday__title {
    font-family: "Anton", sans-serif; font-size: 32px; color: var(--ink); letter-spacing: 1px; line-height: 1.15;
  }
  .holiday__ribbon {
    display: inline-block; margin-top: 4px; padding: 2px 22px;
    background: var(--flag-red); color: var(--white);
    font-family: "Oswald", sans-serif; font-weight: 600; font-size: 13px; letter-spacing: 1px;
  }
  .brand {
    position: absolute; left: 0; right: 0; top: 300px;
    display: flex; align-items: center; justify-content: center; gap: 14px;
  }
  .brand__mark { width: 26px; height: 26px; background: var(--ink); }
  .brand__name {
    font-family: "Oswald", sans-serif; font-weight: 700; font-size: 40px;
    color: var(--ink); letter-spacing: 2px; line-height: 1;
  }
</style>
</head>
<body>
<main class="canvas">

  <section class="postcard postcard--front" aria-label="New Year postcard front">
    <div class="festive-scene" role="img" aria-label="Festive 3D stage with green trees, wrapped gifts, baubles and a round podium under a sky window"></div>
    <div class="greeting">
      <p class="greeting__year">2021</p>
      <p class="greeting__line">HAPPY NEW YEARS</p>
      <p class="greeting__company">MESA FREIGHT CO.</p>
    </div>
    <footer class="front-footer">
      <p class="front-footer__text">Lorem ipsum dolor sit amet, consectetur adipiscing elit, sed do eiusmod tempor incididunt ut labore et dolore magna aliqua. Ut enim ad minim veniam, quis nostrud exercitation ullamco laboris nisi ut aliquip ex ea commodo consequat.</p>
    </footer>
  </section>

  <section class="postcard postcard--back" aria-label="Independence Day postcard back">
    <div class="stamp-box"></div>
    <div class="address-lines"><span></span><span></span><span></span><span></span></div>
    <div class="flags-artwork" role="img" aria-label="Two crossed American flags"></div>
    <p class="faint-year">2021</p>
    <div class="holiday">
      <p class="holiday__country">USA</p>
      <p class="holiday__stars">★★★</p>
      <p class="holiday__title">4TH OF JULY</p>
      <p class="holiday__ribbon">INDEPENDENCE DAY</p>
    </div>
    <div class="brand">
      <span class="brand__mark"></span>
      <span class="brand__name">MESA FREIGHT CO.</span>
    </div>
  </section>

</main>
</body>
</html>
```